TAVRELO GROUP OF CLINICS

We need a medical & lab report file. The design should be healthcare related. Our current file design has been used for almost 10 years. We need something more fresh & up-to-date. We have attached the current file design.

Need extra days to review

```html
<!DOCTYPE html>
<html lang="en">
<head>
<meta charset="utf-8">
<title>Tavrelo Group of Clinics – Medical Report File</title>
<link href="https://fonts.googleapis.com/css2?family=Montserrat:wght@400;600;700;800&family=Great+Vibes&display=swap" rel="stylesheet">
<style>
  :root{
    --bg:#d9dadc;
    --navy:#0f4277;
    --navy-deep:#0a2a4d;
    --night:#061a33;
    --mist:#c7d3df;
    --green:#006a35;
    --cyan:#3ee6ee;
    --white:#ffffff;
    --ring:#a9cbb8;
    --brand:#2e2a86;
  }
  *{box-sizing:border-box;margin:0;padding:0}
  html,body{width:1200px;height:848px;overflow:hidden;background:var(--bg);font-family:"Montserrat",sans-serif}
  .canvas{position:relative;width:1200px;height:848px}
  .cover{position:absolute;top:44px;width:537px;height:760px;overflow:hidden;box-shadow:0 10px 30px rgba(0,0,0,.25)}
  .cover--front{left:48px}
  .cover--back{left:615px}
  .cover svg.art{position:absolute;inset:0;width:100%;height:100%}

  .report-title{position:absolute;left:36px;top:136px;color:var(--cyan);font-weight:800;font-size:26px;letter-spacing:.3px;line-height:1;white-space:nowrap}
  .report-tagline{position:absolute;left:48px;top:164px;color:var(--white);font-family:"Great Vibes",cursive;font-size:24px;line-height:1;white-space:nowrap}
  .report-rule{position:absolute;left:262px;top:182px;width:74px;height:2px;background:var(--white)}

  .privacy-tab{position:absolute;left:28px;top:708px;color:var(--white);line-height:1}
  .privacy-tab strong{display:block;font-weight:800;font-size:24px;letter-spacing:.5px}
  .privacy-tab span{display:block;font-weight:600;font-size:10px;letter-spacing:1px;margin-top:3px}

  .brand-mark{position:absolute;display:flex;align-items:center;justify-content:center;text-align:center;color:var(--brand);font-weight:800;line-height:1.1}
  .cover--front .brand-mark{left:382px;top:492px;width:116px;height:116px;font-size:13px}
  .cover--back .brand-mark{left:108px;top:558px;width:96px;height:96px;font-size:11px}

  .clinic-list{position:absolute;left:220px;top:30px;width:300px;color:var(--white);list-style:none}
  .clinic-list li{margin-bottom:15px;font-size:8.4px;line-height:1.35}
  .clinic-list h3{font-size:9px;font-weight:700;letter-spacing:.3px}
  .clinic-list b{font-weight:700}

  .group-name{position:absolute;left:26px;top:696px;color:var(--white);line-height:1}
  .group-name strong{display:block;font-size:30px;font-weight:800}
  .group-name span{display:block;font-size:17px;font-weight:700;margin-top:2px}
</style>
</head>
<body>
<main class="canvas">

  <section class="cover cover--front" aria-label="Front cover">
    <svg class="art" viewBox="0 0 537 760">
      <defs>
        <linearGradient id="frontSky" x1="0" y1="0" x2="1" y2="0">
          <stop offset="0" stop-color="#b9c6d4"/>
          <stop offset=".28" stop-color="#2c4d72"/>
          <stop offset=".6" stop-color="#0d2f57"/>
          <stop offset="1" stop-color="#0a2a4d"/>
        </linearGradient>
        <linearGradient id="frontShade" x1="0" y1="0" x2="0" y2="1">
          <stop offset="0" stop-color="#061a33" stop-opacity=".7"/>
          <stop offset=".5" stop-color="#061a33" stop-opacity="0"/>
        </linearGradient>
        <linearGradient id="hillTone" x1="0" y1="0" x2="0" y2="1">
          <stop offset="0" stop-color="#27415d" stop-opacity="0"/>
          <stop offset="1" stop-color="#7f93a8" stop-opacity=".8"/>
        </linearGradient>
        <radialGradient id="organTone" cx=".5" cy=".5" r=".6">
          <stop offset="0" stop-color="#f07aa0"/>
          <stop offset=".45" stop-color="#3a74c7"/>
          <stop offset="1" stop-color="#0b2f66"/>
        </radialGradient>
        <linearGradient id="tabTone" x1="0" y1="1" x2="1" y2="0">
          <stop offset="0" stop-color="#b8c6d5"/>
          <stop offset="1" stop-color="#3e6893"/>
        </linearGradient>
      </defs>

      <rect width="537" height="760" fill="url(#frontSky)"/>
      <rect width="537" height="760" fill="url(#frontShade)"/>
      <path role="img" aria-label="Misty mountain range silhouette" d="M0,560 C80,540 160,580 240,530 C300,495 360,520 420,470 L537,420 L537,760 L0,760 Z" fill="url(#hillTone)"/>

      <path d="M334,0 L537,0 L537,500 L470,560 C440,450 400,300 334,0 Z" fill="var(--green)"/>
      <path d="M330,0 C380,220 430,400 470,560" fill="none" stroke="var(--white)" stroke-width="9"/>

      <g fill="none" stroke="var(--white)" stroke-width="4">
        <polyline points="400,116 396,165 368,200"/>
        <polyline points="460,282 456,350 420,380"/>
        <polyline points="180,292 220,318 400,318"/>
        <polyline points="282,460 312,490 452,490"/>
      </g>

      <g stroke="var(--white)" stroke-width="5">
        <polygon role="img" aria-label="Brain scan illustration" points="376,36 424,36 446,75 424,114 376,114 354,75" fill="url(#organTone)"/>
        <polygon role="img" aria-label="Kidney anatomy illustration" points="434,196 486,196 512,240 486,284 434,284 408,240" fill="url(#organTone)"/>
        <polygon role="img" aria-label="Lung anatomy illustration" points="122,207 178,207 206,255 178,303 122,303 94,255" fill="url(#organTone)"/>
        <polygon role="img" aria-label="Heart anatomy illustration" points="220,370 280,370 310,420 280,470 220,470 190,420" fill="url(#organTone)"/>
      </g>

      <path d="M0,650 C190,640 370,580 537,450 L537,760 L0,760 Z" fill="var(--white)"/>
      <path d="M0,760 L0,700 C0,694 4,690 10,690 L180,690 C200,690 206,696 214,710 L226,732 C232,746 240,760 250,760 Z" fill="url(#tabTone)"/>

      <circle cx="440" cy="550" r="62" fill="var(--ring)"/>
      <circle cx="440" cy="550" r="56" fill="var(--white)"/>
    </svg>

    <h1 class="report-title">MEDICAL REPORT</h1>
    <p class="report-tagline">Your healthcare partner</p>
    <div class="report-rule"></div>
    <div class="brand-mark">TAVRELO<br>GROUP</div>
    <div class="privacy-tab"><strong>PRIVATE</strong><span>&amp; CONFIDENTIAL</span></div>
  </section>

  <section class="cover cover--back" aria-label="Back cover">
    <svg class="art" viewBox="0 0 537 760">
      <defs>
        <linearGradient id="backPanel" x1="0" y1="0" x2="1" y2=".4">
          <stop offset="0" stop-color="#7c8ea2"/>
          <stop offset=".4" stop-color="#1d3a5e"/>
          <stop offset="1" stop-color="#0a2240"/>
        </linearGradient>
        <linearGradient id="backHill" x1="0" y1="0" x2="0" y2="1">
          <stop offset="0" stop-color="#1b2d44" stop-opacity="0"/>
          <stop offset="1" stop-color="#2d3d50"/>
        </linearGradient>
        <linearGradient id="nameTab" x1="0" y1="0" x2="1" y2="0">
          <stop offset="0" stop-color="#2f5a88"/>
          <stop offset="1" stop-color="var(--navy)"/>
        </linearGradient>
      </defs>

      <rect width="537" height="760" fill="var(--navy)"/>
      <rect width="208" height="760" fill="url(#backPanel)"/>
      <path role="img" aria-label="Misty mountain range silhouette" d="M0,560 C50,540 100,555 150,520 C180,500 200,510 208,500 L208,760 L0,760 Z" fill="url(#backHill)"/>

      <path d="M0,650 C190,640 370,590 537,520 L537,600 C380,650 220,680 140,690 L20,690 C8,690 0,696 0,706 Z" fill="var(--white)"/>
      <path d="M0,760 L0,706 C0,696 8,690 20,690 L140,690 C220,680 380,650 537,600 L537,760 Z" fill="url(#nameTab)"/>

      <circle cx="156" cy="606" r="58" fill="var(--ring)"/>
      <circle cx="156" cy="606" r="52" fill="var(--white)"/>
    </svg>

    <ul class="clinic-list">
      <li><h3>PUSAT PERUBATAN TAVRELO</h3>Level 12, Wisma Orkid, No.8, Jalan Seri Maju,<br>50480 Kuala Lumpur.<br>Tel No. <b>+603-5550 1201</b> Fax No. <b>+603-5550 1202</b><br>Email : care@tavrelo-clinic.my</li>
      <li><h3>KLINIK TAVRELO (SHAH ALAM)</h3>No.22, Jalan Cempaka 4, Taman Melur,<br>40300 Shah Alam, Selangor.<br>Tel No. <b>+603-5550 2301</b> Fax No. <b>+603-5550 2302</b><br>Email : shahalam@tavrelo-clinic.my</li>
      <li><h3>KLINIK TAVRELO (PENANG)</h3>Lot 5A-2-1, Persiaran Bayu, Taman Nuri,<br>11950 Penang.<br>Tel No. <b>+604-555 3401</b> Fax No. <b>+604-555 3402</b><br>Email : penang@tavrelo-clinic.my</li>
      <li><h3>KLINIK TAVRELO (SEREMBAN)</h3>No.41, Jalan Niaga 2/1, Pusat Niaga Seremban,<br>70450 Seremban, Negeri Sembilan.<br>Tel No. <b>+606-555 4501</b> Fax No. <b>+606-555 4502</b><br>Email : seremban@tavrelo-clinic.my</li>
      <li><h3>TAVRELO MEDICAL CLINIC (TERMINAL 1)</h3>Unit A-05, Arrival Hall, Terminal 1,<br>64000 Sepang, Selangor.<br>Tel No. <b>+603-5550 5601</b> Fax No. <b>+603-5550 5602</b><br>Email : terminal1@tavrelo-clinic.my</li>
      <li><h3>TAVRELO MEDICAL CLINIC (TERMINAL 2)</h3>Unit B-11, Landside Level 2, Terminal 2,<br>64000 Sepang, Selangor.<br>Tel No. <b>+603-5550 6701</b> Fax No. <b>+603-5550 6702</b><br>Email : terminal2@tavrelo-clinic.my</li>
      <li><h3>TAVRELO MEDICAL CLINIC (AIR HUB)</h3>Unit C-03, Level 1, Passenger Terminal,<br>Northern Air Hub, 11900 Penang.<br>Tel No. <b>+604-555 7801</b> Fax No. <b>+604-555 7802</b><br>Email : airhub@tavrelo-clinic.my</li>
    </ul>

    <div class="brand-mark">TAVRELO<br>GROUP</div>
    <div class="group-name"><strong>Tavrelo</strong><span>Group of Clinics</span></div>
  </section>

</main>
</body>
</html>
```